Cortelune Pamphlet

We need to design a pamplet for Cortelune, a Bespoke Wine Cellar design and build company. Our logo and signature cellar should be incorperated into the design (can be seen at www.cortelune-example.com). It should also include what will be called the template with a scematic drawing of a cellar to outline the key features An area called the process will showcase the different types of materials that can be used and there neesa to be indicative costs dependant in size also somewhere, as well as the fact that design £950+VAT but will be taken off the cost of the cellar if we do the job refunded back into project on approval.
.
Updates

Industry/Entity Type

It Company

```html
<!DOCTYPE html>
<html lang="en">
<head>
<meta charset="utf-8">
<title>Cortelune Pamphlet – Inside Spread</title>
<link rel="stylesheet" href="https://fonts.googleapis.com/css2?family=Fira+Sans+Condensed:wght@300;400&family=Sorts+Mill+Goudy&display=swap">
<style>
  :root {
    --page-bg: #ffffff;
    --ink-black: #000000;
    --paper-white: #ffffff;
    --rule-grey: #cfcfcf;
    --render-light: #e4e4e4;
    --render-mid: #b9b9b9;
    --render-dark: #8a8a8a;
    --cellar-blue-deep: #1d2a8f;
    --cellar-blue: #3c52d6;
    --cellar-blue-light: #6f95f0;
    --lounge-olive: #7a8a2c;
    --lounge-dark: #2a2416;
  }
  * { box-sizing: border-box; margin: 0; padding: 0; }
  html, body {
    width: 1200px; height: 846px; overflow: hidden;
    background: var(--page-bg);
  }
  .spread {
    position: absolute; left: 140px; top: 93px;
    width: 920px; height: 660px;
    font-family: "Fira Sans Condensed", "Arial Narrow", sans-serif;
    color: var(--paper-white);
  }
  .panel { position: absolute; top: 0; height: 100%; overflow: hidden; }

  /* Panel 1 – introduction */
  .panel--intro {
    left: 0; width: 230px; background: var(--ink-black);
    padding: 62px 18px 0 18px;
    font-size: 14.5px; line-height: 26px; font-weight: 300;
  }
  .panel--intro p + p { margin-top: 12px; }
  .panel--intro .intro-second { position: absolute; top: 420px; left: 18px; right: 14px; }

  /* Panel 2 – the template */
  .panel--template {
    left: 230px; width: 240px;
    border-left: 2px solid var(--paper-white);
  }
  .template-render {
    position: absolute; inset: 0;
    background: linear-gradient(90deg, var(--render-dark) 0%, var(--render-light) 45%, var(--render-mid) 100%);
  }

  /* Label connector crossing panels 1–2 */
  .connector { position: absolute; left: 18px; top: 396px; overflow: visible; }
  .label {
    position: absolute; background: var(--ink-black);
    font-family: "Sorts Mill Goudy", Georgia, serif;
    letter-spacing: 2px; color: var(--paper-white);
  }
  .label--template { left: 232px; top: 385px; padding: 3px 10px 4px 12px; font-size: 20px; }

  /* Panels 3–4 – the process */
  .panel--process { left: 470px; width: 450px; }
  .cellar-photo {
    position: absolute; inset: 0;
    background: radial-gradient(ellipse at 45% 40%, var(--cellar-blue-light) 0%, var(--cellar-blue) 40%, var(--cellar-blue-deep) 100%);
  }
  .process-box {
    position: absolute; left: 0; top: 320px; width: 206px; bottom: 0;
    background: var(--ink-black);
  }
  .process-band {
    position: absolute; left: 206px; right: 0; top: 555px; bottom: 0;
    background: var(--ink-black);
  }
  .label--process { left: 480px; top: 330px; font-size: 22px; background: none; }
  .process-rules { position: absolute; left: 470px; top: 366px; }
  .process-copy {
    position: absolute; left: 480px; top: 410px; width: 196px;
    font-size: 13.5px; line-height: 27px; font-weight: 300;
  }
  .cost-copy {
    position: absolute; left: 480px; top: 570px; width: 430px;
    font-size: 13.5px; line-height: 27px; font-weight: 300;
  }
  .lounge-photo {
    position: absolute; left: 676px; top: 425px; width: 186px; height: 128px;
    background: linear-gradient(110deg, var(--lounge-olive) 0%, #a9b85a 35%, var(--lounge-dark) 75%);
  }
</style>
</head>
<body>
  <main class="spread">
    <section class="panel panel--intro">
      <p>Cortelune combines custom artistic home wine cellar design with elegance and engineering to produce wine storage known for its extravagance, architecture and identity.</p>
      <p>Specialising in concept imagery, design and fabrication of bespoke wine cellars.</p>
      <p class="intro-second">We combine artistic design with imagination, elegance and engineering to produce spaces known for their extravagance, architecture and identity.</p>
    </section>

    <section class="panel panel--template">
      <div class="template-render" role="img" aria-label="Grey schematic render of the template cellar: upright racks, round bottle cubbies and stepped shelving"></div>
    </section>

    <svg class="connector" width="240" height="40" aria-hidden="true">
      <polyline points="0,34 170,30" fill="none" stroke="var(--rule-grey)" stroke-width="1"/>
      <polyline points="100,32 100,12 214,10" fill="none" stroke="var(--rule-grey)" stroke-width="1"/>
    </svg>
    <div class="label label--template">the template</div>

    <section class="panel panel--process">
      <div class="cellar-photo" role="img" aria-label="Signature cellar photo: blue-lit gothic arches lined with bottle racks"></div>
      <div class="process-box"></div>
      <div class="process-band"></div>
    </section>

    <h2 class="label label--process">the process</h2>
    <svg class="process-rules" width="200" height="40" aria-hidden="true">
      <line x1="10" y1="6" x2="192" y2="6" stroke="var(--rule-grey)" stroke-width="1"/>
      <line x1="100" y1="6" x2="100" y2="36" stroke="var(--rule-grey)" stroke-width="1"/>
      <line x1="10" y1="36" x2="192" y2="36" stroke="var(--rule-grey)" stroke-width="1"/>
    </svg>
    <p class="process-copy">Rich hard wood, hand stitched leather beautiful ambience driven lighting displays with seamless finishes to display your magnificent collection of wines, champagnes and spirits.</p>
    <div class="lounge-photo" role="img" aria-label="Photo of a warmly lit cellar lounge with wall-mounted wine bottles"></div>
    <p class="cost-copy">Indicative costs are dependant on size. Design £950+VAT, will be taken off the cost of the cellar if we do the job, and refunded back into the project on approval.</p>
  </main>
</body>
</html>
```